Stationary set for consulting company
Tarvo Bridge
Creative Brief
Modern
Karim Yusuf Al Banna
Co-Founder
Reef Spire, Abu Dhabi United Arab Emirates
karim@tarvobridge.ae
www.tarvobridge.com
I need a full stationary set for the company logo I will be attaching. (PPTs, business cards, envelope, letterhead, etc)

```html
<!DOCTYPE html>
<html lang="en">
<head>
<meta charset="utf-8">
<title>Tarvo Bridge Consulting – Business Card</title>
<link rel="stylesheet" href="https://fonts.googleapis.com/css2?family=Roboto:wght@400;500;700&display=swap">
<style>
  :root {
    --page-bg: #e6e6e6;
    --brand-blue: #2d4a8a;
    --brand-blue-deep: #243d74;
    --brand-blue-mark: #213868;
    --card-white: #ffffff;
    --text-grey: #8a8f99;
    --divider: #c9ccd3;
  }
  * { margin: 0; padding: 0; box-sizing: border-box; }
  html, body {
    width: 1200px;
    height: 901px;
    overflow: hidden;
    background: var(--page-bg);
    font-family: "Roboto", Arial, sans-serif;
  }
  .canvas { position: relative; width: 1200px; height: 901px; }

  .card {
    position: absolute;
    left: 299px;
    width: 601px;
    border-radius: 14px;
    overflow: hidden;
  }

  /* Back side */
  .card-back {
    top: 68px;
    height: 346px;
    background: var(--brand-blue);
    display: flex;
    align-items: center;
    justify-content: center;
  }
  .back-wordmark {
    display: flex;
    align-items: center;
    gap: 18px;
    color: var(--brand-blue-mark);
    font-weight: 700;
    font-size: 46px;
    letter-spacing: 1px;
  }
  .back-wordmark .mark-square {
    width: 58px; height: 58px;
    background: var(--brand-blue-mark);
  }

  /* Front side */
  .card-front {
    top: 553px;
    height: 279px;
    background: var(--card-white);
  }
  .front-wordmark {
    position: absolute;
    left: 22px;
    top: 133px;
    display: flex;
    align-items: center;
    gap: 10px;
    color: var(--brand-blue);
    font-weight: 700;
    font-size: 25px;
  }
  .front-wordmark .mark-square {
    width: 30px; height: 30px;
    background: var(--brand-blue);
  }
  .divider {
    position: absolute;
    left: 300px;
    top: 32px;
    width: 1px;
    height: 134px;
    background: var(--divider);
  }
  .identity {
    position: absolute;
    left: 317px;
    top: 38px;
  }
  .person-name {
    color: var(--brand-blue);
    font-weight: 700;
    font-size: 21px;
    line-height: 1.2;
  }
  .person-role {
    color: var(--text-grey);
    font-size: 13px;
    margin-top: 3px;
  }
  .contact-list {
    list-style: none;
    margin-top: 26px;
  }
  .contact-list li {
    display: flex;
    align-items: center;
    gap: 8px;
    color: var(--text-grey);
    font-size: 13px;
    height: 20px;
  }
  .contact-list svg { width: 11px; height: 11px; fill: var(--brand-blue); }
  .address-band {
    position: absolute;
    left: 0; bottom: 0;
    width: 100%;
    height: 34px;
    background: var(--brand-blue);
    color: #ffffff;
    font-size: 12px;
    display: flex;
    align-items: center;
    justify-content: center;
  }
</style>
</head>
<body>
<div class="canvas">
  <section class="card card-back" aria-label="Card back">
    <div class="back-wordmark"><span class="mark-square"></span>Tarvo Bridge</div>
  </section>

  <section class="card card-front" aria-label="Card front">
    <div class="front-wordmark"><span class="mark-square"></span>Tarvo Bridge</div>
    <div class="divider"></div>
    <div class="identity">
      <h1 class="person-name">Karim Yusuf Al Banna</h1>
      <p class="person-role">Co-Founder</p>
      <ul class="contact-list">
        <li>
          <svg viewBox="0 0 24 24" aria-hidden="true"><path d="M6.6 10.8a15.1 15.1 0 0 0 6.6 6.6l2.2-2.2a1 1 0 0 1 1-.25 11.4 11.4 0 0 0 3.6.57 1 1 0 0 1 1 1V20a1 1 0 0 1-1 1A17 17 0 0 1 3 4a1 1 0 0 1 1-1h3.5a1 1 0 0 1 1 1c0 1.25.2 2.45.57 3.57a1 1 0 0 1-.25 1z"/></svg>
          +971-50-3190452
        </li>
        <li>
          <svg viewBox="0 0 24 24" aria-hidden="true"><path d="M2 5h20v14H2z M2 5l10 8 10-8" fill="none" stroke="#2d4a8a" stroke-width="2.4"/></svg>
          karim@tarvobridge.ae
        </li>
        <li>
          <svg viewBox="0 0 24 24" aria-hidden="true"><circle cx="12" cy="12" r="10" fill="none" stroke="#2d4a8a" stroke-width="2.4"/><path d="M2 12h20M12 2c3 3 3 17 0 20M12 2c-3 3-3 17 0 20" fill="none" stroke="#2d4a8a" stroke-width="1.8"/></svg>
          www.tarvobridge.com
        </li>
      </ul>
    </div>
    <div class="address-band">Reef Spire, Abu Dhabi, United Arab Emirates</div>
  </section>
</div>
</body>
</html>
```